Professional DJ Business Card

Business card for giving out to clubs and venues or interested groups that are in need of a professional DJ. I want something artistic and catchy/alluring, with a minimalist approach that gets just the vital amount of info and leaves the rest for inquiry via contacting me. Ideally I would like one side to have an image of something cool like an eye and my name, then the other side be the contact info, I am definitely feeling a black or dark colored card, but I am open to other designs. I am uploading a picture that I made that reflects a little of what I am *kind of* looking for.

Industry/Entity Type

Business

Contact Information for Business Card

Tomas Halvik (Voxtel)
Professional DJ (West Coast)
EDM (Deep/House/Techno), Hip Hop, Latin, Trap.
Cell: 555-274-9163
Email: Voxtelofficial@mailnest.net
www.beatcloudia.net/yourtuneisfading

```html
<!DOCTYPE html>
<html lang="en">
<head>
<meta charset="utf-8">
<title>Voxtel – DJ Business Card</title>
<link href="https://fonts.googleapis.com/css2?family=Open+Sans:wght@400;600;700&family=Permanent+Marker&family=Tinos:ital@1&display=swap" rel="stylesheet">
<style>
  :root {
    --page-bg: #eeeeef;
    --card-black: #0b0c0b;
    --card-edge: #1d1c3a;
    --ink-white: #f4f4f4;
    --band-grey: #a6a6a6;
    --band-ink: #1a1a1a;
    --art-mid: #3a3a3a;
  }
  * { box-sizing: border-box; margin: 0; padding: 0; }
  html, body { width: 1200px; height: 1200px; overflow: hidden; background: var(--page-bg); }
  body { position: relative; font-family: "Open Sans", sans-serif; color: var(--ink-white); }

  .card {
    position: absolute;
    left: 200px;
    width: 800px;
    height: 457px;
    background: var(--card-black);
    overflow: hidden;
  }
  .card--front { top: 110px; border: 2px solid var(--card-edge); }
  .card--back { top: 633px; }

  /* Front side */
  .front-art {
    position: absolute;
    left: 180px; top: 60px;
    width: 420px; height: 300px;
    background: radial-gradient(ellipse at 50% 60%, var(--art-mid) 0%, rgba(40,40,40,0.5) 35%, transparent 70%);
  }
  .front-name {
    position: absolute;
    top: 66px; left: 0; right: 0;
    text-align: center;
    font-family: "Permanent Marker", cursive;
    font-size: 52px;
    letter-spacing: 2px;
  }
  .front-role {
    position: absolute;
    top: 140px; left: 0; right: 0;
    text-align: center;
    font-family: "Tinos", serif;
    font-style: italic;
    font-size: 25px;
  }
  .genre-band {
    position: absolute;
    top: 232px; left: 50px; right: 50px;
    height: 50px;
    background: var(--band-grey);
    color: var(--band-ink);
    font-weight: 600;
    font-size: 23px;
    display: flex; align-items: center; justify-content: center;
  }
  .contact-row {
    position: absolute;
    top: 340px; left: 0; right: 0;
    display: flex; align-items: center; justify-content: center;
    gap: 26px;
    font-size: 21px;
  }
  .contact-item { display: flex; align-items: center; gap: 10px; }
  .contact-divider { width: 2px; height: 44px; background: var(--ink-white); }
  .contact-icon { width: 26px; height: 26px; }

  /* Back side */
  .back-art {
    position: absolute;
    left: 230px; top: 30px;
    width: 340px; height: 260px;
    background: radial-gradient(ellipse at 50% 50%, #2c2c2c 0%, #161616 50%, transparent 75%);
  }
  .brand-mark {
    position: absolute;
    top: 180px; left: 0; right: 0;
    display: flex; align-items: center; justify-content: center; gap: 18px;
  }
  .brand-dot { width: 26px; height: 26px; border-radius: 50%; background: var(--ink-white); }
  .brand-name {
    font-family: "Open Sans", sans-serif;
    font-weight: 700;
    font-size: 84px;
    letter-spacing: 3px;
    color: var(--ink-white);
  }
  .web-row {
    position: absolute;
    top: 360px; left: 0; right: 0;
    display: flex; align-items: center; justify-content: center; gap: 14px;
    font-size: 22px;
  }
</style>
</head>
<body>
  <section class="card card--front">
    <div class="front-art" role="img" aria-label="Faint brushed eye illustration behind the name"></div>
    <h1 class="front-name">Tomas Halvik (Voxtel)</h1>
    <p class="front-role">Professional DJ (West Coast)</p>
    <div class="genre-band">EDM (Deep / House / Techno), Hip Hop, Latin, Trap</div>
    <div class="contact-row">
      <span class="contact-item">
        <svg class="contact-icon" viewBox="0 0 24 24" aria-hidden="true">
          <path d="M6 2h3l1.5 5-2 1.5a12 12 0 0 0 7 7l1.5-2 5 1.5v3a2 2 0 0 1-2 2A19 19 0 0 1 4 4a2 2 0 0 1 2-2z" fill="#f4f4f4"/>
        </svg>
        555-274-9163
      </span>
      <span class="contact-divider"></span>
      <span class="contact-item">
        <svg class="contact-icon" viewBox="0 0 24 24" aria-hidden="true">
          <circle cx="12" cy="12" r="11" fill="#f4f4f4"/>
          <rect x="6" y="8" width="12" height="8" fill="none" stroke="#0b0c0b" stroke-width="1.6"/>
          <path d="M6 8l6 5 6-5" fill="none" stroke="#0b0c0b" stroke-width="1.6"/>
        </svg>
        Voxtelofficial@mailnest.net
      </span>
    </div>
  </section>

  <section class="card card--back">
    <div class="back-art" role="img" aria-label="Brushed eye illustration with sweeping lines"></div>
    <div class="brand-mark">
      <span class="brand-dot"></span>
      <span class="brand-name">Voxtel</span>
    </div>
    <div class="web-row">
      <svg class="contact-icon" viewBox="0 0 24 24" aria-hidden="true">
        <g fill="none" stroke="#f4f4f4" stroke-width="1.6">
          <circle cx="12" cy="12" r="10"/>
          <ellipse cx="12" cy="12" rx="4.5" ry="10"/>
          <path d="M2 12h20M4 7h16M4 17h16"/>
        </g>
      </svg>
      www.beatcloudia.net/yourtuneisfading
    </div>
  </section>
</body>
</html>
```